Business Card Design

I need a business card design for my law office based in Pasadena, California. I am a sole practitioner and I specialize in business transaction and litigation, probate and estate planning, taxation law, corporate and business formation, immigration and real estate. I want something that is simple, yet stands out.

A friend helped to create a logo about 6 years ago. I am open to new ideas to changing the logo.

Industry/Entity Type

Business

Contact Information for Business Card

Law Offices of Dorvan L. Mabry
842 W. Larkspur Ave., Suite 319
Pasadena, CA 90287
Tel: 626-555-0174
Fax: 626-555-0139
Email: dmabry@dlmlegalgroup.example

Attorney: Dorvan L. Mabry

```html
<!DOCTYPE html>
<html lang="en">
<head>
<meta charset="utf-8">
<title>Law Offices of Dorvan L. Mabry — Business Card</title>
<link rel="stylesheet" href="https://fonts.googleapis.com/css2?family=Source+Sans+3:wght@400;600&display=swap">
<style>
  :root {
    --backdrop: #e9e6e1;
    --card-dark: #1f1e1f;
    --card-light: #ffffff;
    --ink: #1a1a1a;
    --ink-soft: #333333;
    --rule-dark: #8c8c8c;
    --rule-light: #3a3a3a;
    --mark-light: #d9d9d9;
  }
  * { box-sizing: border-box; margin: 0; padding: 0; }
  html, body {
    width: 1200px; height: 900px; overflow: hidden;
    background: var(--backdrop);
    font-family: "Source Sans 3", "Myriad Pro", Arial, sans-serif;
  }
  .stage {
    width: 1200px; height: 900px;
    display: flex; align-items: center; justify-content: center; gap: 40px;
  }
  .card {
    width: 540px; height: 309px; position: relative;
    box-shadow: 0 6px 18px rgba(0,0,0,.18);
  }
  /* Front: dark */
  .card--front { background: var(--card-dark); }
  .front-wordmark {
    position: absolute; left: 100px; right: 70px; top: 112px;
    color: var(--mark-light); text-transform: uppercase; font-weight: 400;
  }
  .front-wordmark .rule {
    border-top: 1px solid var(--rule-dark); margin-bottom: 6px;
  }
  .front-wordmark .rule--top { margin-left: 40px; margin-right: 30px; }
  .front-wordmark .kicker {
    display: block; font-size: 10px; letter-spacing: 6px; margin: 0 0 4px 44px;
  }
  .front-wordmark .name {
    display: block; font-size: 34px; letter-spacing: 2px; line-height: 1;
  }
  /* Back: light */
  .card--back { background: var(--card-light); color: var(--ink); }
  .contact {
    position: absolute; left: 315px; top: 22px; font-size: 11.5px; line-height: 1.3;
  }
  .contact .person { font-weight: 600; font-size: 14px; line-height: 1.1; }
  .contact .role { font-size: 10px; margin-bottom: 14px; }
  .contact .firm { font-weight: 600; font-size: 11.5px; }
  .contact address { font-style: normal; margin-bottom: 14px; }
  .contact ul { list-style: none; }
  .contact li { display: flex; align-items: center; gap: 8px; margin-bottom: 3px; }
  .contact svg { width: 10px; height: 10px; fill: var(--ink); flex: none; }
  .back-wordmark {
    position: absolute; left: 26px; right: 240px; top: 190px;
    color: var(--ink-soft); text-transform: uppercase; font-weight: 400;
  }
  .back-wordmark .badge {
    width: 26px; height: 26px; background: var(--ink-soft); margin: 0 0 10px 110px;
  }
  .back-wordmark .kicker {
    display: block; font-size: 9px; letter-spacing: 5px; margin: 0 0 3px 40px;
  }
  .back-wordmark .rule { border-top: 1px solid var(--rule-light); margin-bottom: 5px; }
  .back-wordmark .name {
    display: block; font-size: 25px; letter-spacing: 1.5px; line-height: 1; white-space: nowrap;
  }
</style>
</head>
<body>
<main class="stage">
  <section class="card card--front" aria-label="Card front">
    <div class="front-wordmark">
      <span class="kicker">Law Offices of</span>
      <div class="rule"></div>
      <span class="name">Dorvan L. Mabry</span>
    </div>
  </section>

  <section class="card card--back" aria-label="Card back">
    <div class="contact">
      <p class="person">Dorvan L. Mabry</p>
      <p class="role">Attorney</p>
      <p class="firm">Law Offices of Dorvan L. Mabry</p>
      <address>842 W. Larkspur Ave., Suite 319<br>Pasadena, CA 90287</address>
      <ul>
        <li><svg viewBox="0 0 10 10" aria-label="Telephone"><path d="M2 0.5l1.8 2-0.9 1.1c0.6 1.3 1.4 2.1 2.6 2.7l1.1-0.9 2 1.8-1.2 1.8C4.3 8.6 1.4 5.8 0.4 1.7z"/></svg>626-555-0174</li>
        <li><svg viewBox="0 0 10 10" aria-label="Fax"><rect x="2.5" y="0.5" width="5" height="3"/><rect x="0.5" y="3.5" width="9" height="5" rx="1"/><rect x="2.5" y="6.5" width="5" height="3" fill="#fff"/></svg>626-555-0139</li>
        <li><svg viewBox="0 0 10 10" aria-label="Email"><rect x="0.5" y="2" width="9" height="6.5"/><path d="M0.8 2.3L5 5.6 9.2 2.3" fill="none" stroke="#fff" stroke-width="0.9"/></svg>dmabry@dlmlegalgroup.example</li>
      </ul>
    </div>
    <div class="back-wordmark">
      <div class="badge"></div>
      <div class="rule"></div>
      <span class="kicker">Law Offices of</span>
      <div class="rule"></div>
      <span class="name">Dorvan L. Mabry</span>
    </div>
  </section>
</main>
</body>
</html>
```